Stationery Design Project

We need a stationery design for our Norwegian trucking company. We have existed for about 15 years and our 12 drivers uses relatively new vehicles to transport goods around in northern Norway. Long distance routes with fresh fish og food transport is our main operations.

We have already made alogo that's printed on our trucks. The logo and a picture of our trucks is attached. I think the logo i crappy, but since its already in use, changing it is not an option in this round. Still using a better colour scheme in the overall stationery and more interesting fonts is possible (altso in the logo).

Company details:
Name: Vikstrandbil AS
Organisation nr 981 537 608
Post adress: 8613 Lysvær

I like minimalism and simplicity. I am avalibly for questions in normal GMT working hours either here or on mail: petter@vikstrand.no

Reason: Hi. Im extending the deadline because I needed some time to find a vector file of our logo. Sorry for the inconvenience

Hi, and thanks for all your interest in the project. Some updates:

-          I have decided to commit to using one of the designs. Some designer will get the payment.

-          I have extended the deadline with 24 hours since I needed some time to find our firms vector logo (a slow Swedish man was holding me up)

-          We will not choose a design before the deadline. No need to rush.

-          We have received a lot of great design and think there is a need to specified the product we want to make:

o   Business Card for all our employers. I just need the design and will duplicate with the correct numbers and name myself. The information on should be: Logo, employer’s name, Phone number, email, website, Postal number and address. Use this as a template: logo, Leif Brattli, 47283916, Leif@vikstrand.no,, vikstrand.no, 8613 Lysvær. The order and placement of the information is your creative decision.

o   Stickers to put on the goods we travel. On the sticker the should be the following information: Logo, phone number, Tekst and link: Fraktæ av Vikstrandbil. Ke du syns? Vikstrand.no/tilbakemelding (this means: Handled by Vikstrandbil. What do you think Vikstrand.no/feedback -à the link will be a feedback form). The placement the information and size is your creative decision with some stings: we have been thinking of using Prentavo for printing and see that a size about 6x6 cm, 8x5 or something like that. (with 3000 copies our budget is 200 punds). Any suggestions of other suppliers are welcome. Prentavo price calculator http://www.prentavoprint.co.uk/digital-litho-printing/printing-labels-tags/stickers/

o   Letterhead with logo, address, phone number and organizational number.

o   Envelopes with logo,address, phone number and organizational number.

Have a nice day.

 

 

• Using the blue colour in the logo and using a similar graphic approch.

```html
<!DOCTYPE html>
<html lang="no">
<head>
<meta charset="utf-8">
<title>Vikstrandbil – visittkort</title>
<link rel="stylesheet" href="https://fonts.googleapis.com/css2?family=Open+Sans:wght@400;600;700&display=swap">
<style>
  :root {
    --backdrop: #d9dbde;
    --paper: #ffffff;
    --brand-blue: #0d55a8;
    --brand-sky: #0a74ba;
    --brand-navy: #0a4f9f;
    --ink: #3a3a3a;
    --rule: #9aa7b8;
    --on-dark: #ffffff;
  }
  * { margin: 0; padding: 0; box-sizing: border-box; }
  html, body { width: 1200px; height: 732px; overflow: hidden; }
  body {
    background: var(--backdrop);
    font-family: "Open Sans", Arial, sans-serif;
    position: relative;
  }
  .card {
    position: absolute;
    width: 519px;
    height: 296px;
    box-shadow: 0 1px 3px rgba(0,0,0,.25);
  }
  .card--front { left: 63px;  top: 45px;  background: var(--paper); }
  .card--white { left: 617px; top: 43px;  background: var(--paper); }
  .card--sky   { left: 66px;  top: 386px; background: var(--brand-sky); }
  .card--navy  { left: 616px; top: 382px; background: var(--brand-navy); }

  .wordmark {
    position: absolute;
    left: 0; right: 0;
    display: flex;
    align-items: center;
    justify-content: center;
    gap: 12px;
    font-weight: 700;
    font-size: 42px;
    letter-spacing: -0.5px;
    color: var(--brand-blue);
  }
  .wordmark__dot {
    width: 22px; height: 22px;
    border-radius: 50%;
    background: currentColor;
  }
  .card--front .wordmark { top: 62px; }
  .card--white .wordmark,
  .card--sky .wordmark,
  .card--navy .wordmark { top: 118px; }
  .card--sky .wordmark,
  .card--navy .wordmark { color: var(--on-dark); }

  .website {
    position: absolute;
    left: 0; right: 0;
    top: 248px;
    text-align: center;
    font-size: 16px;
    letter-spacing: 3.5px;
    color: var(--ink);
  }
  .card--sky .website,
  .card--navy .website { color: var(--on-dark); }

  .contact {
    position: absolute;
    top: 205px;
    left: 0;
    width: 100%;
    font-size: 14px;
    line-height: 20px;
    color: var(--ink);
  }
  .contact__person {
    position: absolute;
    right: 242px;
    text-align: right;
  }
  .contact__name {
    font-weight: 700;
    font-size: 17px;
    color: var(--brand-blue);
    margin-bottom: 2px;
    line-height: 22px;
  }
  .contact__divider {
    position: absolute;
    left: 287px;
    top: 0;
    width: 1px;
    height: 66px;
    background: var(--rule);
  }
  .contact__company {
    position: absolute;
    left: 300px;
  }
  .contact__org { line-height: 22px; margin-bottom: 2px; }
  .contact__org-label { color: var(--brand-blue); font-size: 15px; }
  .contact__line { display: flex; align-items: center; gap: 5px; }
  .contact__person .contact__line { justify-content: flex-end; }
  .icon { width: 11px; height: 11px; fill: var(--brand-blue); flex: none; }
</style>
</head>
<body>

  <section class="card card--front" aria-label="Visittkort forside">
    <div class="wordmark"><span class="wordmark__dot"></span>Vikstrandbil</div>
    <div class="contact">
      <div class="contact__person">
        <div class="contact__name">Leif Brattli</div>
        <div class="contact__line">
          <svg class="icon" viewBox="0 0 12 12" aria-hidden="true"><path d="M6 1 L11 5 L10 5 L10 11 L2 11 L2 5 L1 5 Z"/></svg>
          <span>8613 Lysvær</span>
        </div>
        <div class="contact__line">
          <svg class="icon" viewBox="0 0 12 12" aria-hidden="true"><path d="M3 1 L5 1 L6 4 L4.5 5 C5 6.5 5.8 7.3 7 7.8 L8 6.3 L11 7.3 L11 9.5 C11 10.4 10.2 11 9.3 11 C4.8 10.6 1.4 7.2 1 2.8 C1 1.8 1.8 1 3 1 Z"/></svg>
          <span>47283916</span>
        </div>
      </div>
      <div class="contact__divider"></div>
      <div class="contact__company">
        <div class="contact__org"><span class="contact__org-label">Org nr</span> 981 537 608</div>
        <div class="contact__line">
          <svg class="icon" viewBox="0 0 12 12" aria-hidden="true"><path d="M1 3 L11 3 L11 10 L1 10 Z M1.8 3.6 L6 7 L10.2 3.6" stroke="#fff" stroke-width=".8"/></svg>
          <span>Leif@vikstrand.no</span>
        </div>
        <div class="contact__line">
          <svg class="icon" viewBox="0 0 12 12" aria-hidden="true"><circle cx="6" cy="6" r="5"/><path d="M1 6 H11 M6 1 C3.5 3.5 3.5 8.5 6 11 M6 1 C8.5 3.5 8.5 8.5 6 11" stroke="#fff" stroke-width=".8" fill="none"/></svg>
          <span>www.vikstrand.no</span>
        </div>
      </div>
    </div>
  </section>

  <section class="card card--white" aria-label="Visittkort bakside, hvit">
    <div class="wordmark"><span class="wordmark__dot"></span>Vikstrandbil</div>
    <div class="website">www.vikstrand.no</div>
  </section>

  <section class="card card--sky" aria-label="Visittkort bakside, lyseblå">
    <div class="wordmark"><span class="wordmark__dot"></span>Vikstrandbil</div>
    <div class="website">www.vikstrand.no</div>
  </section>

  <section class="card card--navy" aria-label="Visittkort bakside, mørkeblå">
    <div class="wordmark"><span class="wordmark__dot"></span>Vikstrandbil</div>
    <div class="website">www.vikstrand.no</div>
  </section>

</body>
</html>
```